Northern Terrain Published Photographer Website

I need a website to feature a home page slide show of 6 of my top photos then a few simple pages including; gallery, bio, social, checkout, services
Updates

Need extra days to review

Target Market(s)

photography

Industry/Entity Type

Photographer

Coding

Coded - Design and coding required

Number of Pages Required

5+ page

Colors

Designer to choose colors to be used in the design.

Requirements
Must have
• clean eye catching elegant trendy
Nice to have
• unique and creative from other photographer websites

```html
<!DOCTYPE html>
<html lang="en">
<head>
<meta charset="utf-8">
<title>Marisa Holloway Photography</title>
<link href="https://fonts.googleapis.com/css2?family=Poppins:wght@400;500;600&family=Great+Vibes&display=swap" rel="stylesheet">
<style>
:root{
  --bg:#171717;
  --bg-dark:#121212;
  --white:#ffffff;
  --muted:#bdbdbd;
  --line:#6a6a6a;
  --field-line:#4a4a4a;
}
*{margin:0;padding:0;box-sizing:border-box}
html,body{width:1200px;height:3591px;overflow:hidden;background:var(--bg);font-family:'Poppins',sans-serif;color:var(--white)}
.page{position:relative;width:1200px;height:3591px;overflow:hidden}
.abs{position:absolute}
.script{font-family:'Great Vibes',cursive;font-weight:400}

.hero{left:0;top:0;width:1200px;height:626px;background:linear-gradient(180deg,#6e2e22 0%,#d9501f 14%,#f39a2a 24%,#e8673a 32%,#3a2a3a 42%,#2b2f3f 50%,#8f8fc8 62%,#c8c6ef 72%,#7570a8 84%,#3e3040 100%)}
.navbar{left:0;top:0;width:1200px;height:49px;background:rgba(20,20,20,.85)}
.brand{left:109px;top:0;width:209px;height:77px;background:#0b0b0b;border:2px solid #2d2d2d;display:flex;align-items:center;justify-content:center;font-size:15px;font-weight:500;letter-spacing:.5px}
.menu{left:464px;top:18px;display:flex;gap:38px;font-size:11px;letter-spacing:.3px}
.social{display:flex;gap:7px}
.social span{width:25px;height:25px;border:1.3px solid var(--white);border-radius:50%;display:block}
.nav-social{left:966px;top:13px}
.arrow{top:290px}
.dots{left:555px;top:604px;display:flex;gap:7px}
.dots span{width:9px;height:9px;border:1px solid var(--white);border-radius:50%}
.dots .on{background:var(--white)}

.portrait{left:0;top:690px;width:244px;height:342px;background:linear-gradient(180deg,#e5d6a4 0%,#d8b98a 40%,#6c6c70 70%,#3d3d42 100%);border-radius:110px 110px 0 0}
.welcome-kicker{left:361px;top:697px;font-size:14px;font-weight:500}
.welcome-title{left:359px;top:716px;font-size:36px}
.welcome-text{left:361px;top:775px;width:630px;font-size:9.6px;line-height:20px;color:#e6e6e6}
.welcome-text p{margin-bottom:4px}
.btn{border:1px solid var(--white);border-radius:20px;display:flex;align-items:center;justify-content:center;font-size:10px;font-weight:500;letter-spacing:.3px}
.btn-contact{left:360px;top:937px;width:138px;height:29px}

.services{left:0;top:1032px;width:1200px;height:485px;background:radial-gradient(ellipse at 50% 45%,#4a4a4a 0%,#333 40%,#2a2a22 75%,#1e211b 100%)}
.sec-title{width:1200px;text-align:center;font-size:38px}
.sec-sub{font-size:10px;font-weight:500}
.card{overflow:hidden}
.card .photo{width:100%;height:100%}
.card .label{position:absolute;left:0;right:0;bottom:34px;height:27px;background:rgba(15,15,15,.85);display:flex;align-items:center;justify-content:center;font-size:12px;font-weight:600;letter-spacing:1.5px}
.card-feature .label{bottom:32px;height:58px;background:rgba(240,240,240,.88);color:#333;font-size:15px;line-height:19px;text-align:center;letter-spacing:1.5px}

.filters{left:0;top:1673px;width:1200px;display:flex;justify-content:center;gap:36px;font-size:10px;color:var(--muted)}
.filters .active{color:var(--white);border-bottom:1px solid var(--white);padding-bottom:3px}
.tile{position:absolute}
.btn-gallery{left:523px;top:2416px;width:152px;height:29px}

.insta{left:0;top:2580px;width:1200px;height:197px;display:flex;gap:2px}
.insta div{flex:1}
.btn-follow{left:524px;top:2805px;width:151px;height:35px;font-size:11px}

.contact{left:0;top:2902px;width:1200px;height:420px;background:linear-gradient(180deg,#2b2b2b 0%,#3a3a3a 35%,#2e2b28 65%,#4a3a2c 80%,#1e1e1e 100%)}
.field{background:rgba(25,25,25,.8);border:1px solid var(--field-line);font-size:9.5px;color:#8a8a8a;padding:0 19px;display:flex;align-items:center}
.field.tall{align-items:flex-start;padding-top:15px}
.field .icon{position:absolute;right:0;top:0;bottom:0;width:40px;border-left:1px solid var(--field-line);display:flex;align-items:center;justify-content:center}
.btn-submit{left:525px;top:3213px;width:150px;height:35px;background:var(--white);color:#111;border:none;font-size:11px}

.footer{left:0;top:3322px;width:1200px;height:230px;background:var(--bg)}
.foot-text{font-size:12.5px;font-weight:500;text-align:center}
.foot-rule{height:1px;background:var(--line)}
.foot-div{width:1px;height:112px;top:3380px;background:var(--line)}
.bottom{left:0;top:3552px;width:1200px;height:39px;background:var(--bg-dark)}
.cards{display:flex;gap:5px}
.cards span{width:31px;height:18px;background:#e9e9e9;border-radius:2px;display:block}
</style>
</head>
<body>
<div class="page">

  <div class="abs hero" role="img" aria-label="Slideshow photo: fiery orange sunset sky over snow-covered cliffs and pine trees"></div>
  <div class="abs navbar"></div>
  <div class="abs brand">Marisa Holloway</div>
  <nav class="abs menu"><span>ABOUT ME</span><span>SERVICES</span><span>MY GALLERY</span><span>CHECKOUT</span><span>CONTACT ME</span></nav>
  <div class="abs social nav-social" aria-label="Social links"><span></span><span></span><span></span><span></span></div>
  <svg class="abs arrow" style="left:18px" width="24" height="56" viewBox="0 0 24 56"><path d="M22 2 L3 28 L22 54" fill="none" stroke="#fff" stroke-width="1.6"/></svg>
  <svg class="abs arrow" style="left:1156px" width="24" height="56" viewBox="0 0 24 56"><path d="M2 2 L21 28 L2 54" fill="none" stroke="#fff" stroke-width="1.6"/></svg>
  <div class="abs dots"><span></span><span class="on"></span><span></span><span></span><span></span><span></span></div>

  <div class="abs portrait" role="img" aria-label="Portrait of the photographer with long blonde hair in a sparkly grey dress"></div>
  <div class="abs welcome-kicker">WELCOME TO THE</div>
  <div class="abs welcome-title script">Marisa Holloway Photography</div>
  <div class="abs welcome-text">
    <p>Lorem ipsum dolor sit amet, consectetur adipiscing elit. Phasellus elit felis, fringilla non vehicula ut, vehicula bibendum orem ipsum dolor maurisehicula bibendum mauris</p>
    <p>Lorem ipsum dolor sit amet, consectetur adipiscing elit. Phasellus elit felis, fringilla non vehicula ut, vehicula bibendum mauris. oltoe Vivamus placerat sit amet nunc ut ornare. Nam sed erat sit amet massa aliquam lobortis id vel justo. Aliquam ac malesuadaasds itsa tellus.asd Curabitur eu felis id ligula ultrices tincidunt.Lorem ipsum dolor sit amet, consectetur adipiscing elit. Phasellus elit feli loriw, fringilla non vehicula ut, vehicula bibendum mauris. Vivamus placerat sit amet nunc ut ornare. Nam sed erat sit amet massa aliqama lobortis id vel justo. Aliquam ac malesuada tellus.asd Curabitur eu felis id ligula ultrices tincidunt.</p>
  </div>
  <div class="abs btn btn-contact">CONTACT ME NOW</div>

  <div class="abs services" role="img" aria-label="Blurred dark forest background"></div>
  <div class="abs sec-title script" style="left:-30px;top:1090px">Photography Services</div>
  <div class="abs sec-sub" style="left:691px;top:1136px">PROVIDES FOR</div>

  <div class="abs card" style="left:117px;top:1195px;width:170px;height:238px">
    <div class="photo" role="img" aria-label="Horseshoe bend canyon with river" style="background:linear-gradient(180deg,#8aa3c4 0%,#a56a4a 30%,#7a3f2a 60%,#3f6b5e 85%,#5a3a2a 100%)"></div>
    <div class="label">NATURE</div>
  </div>
  <div class="abs card card-feature" style="left:302px;top:1174px;width:222px;height:280px">
    <div class="photo" role="img" aria-label="Bighorn sheep in a desert field" style="background:linear-gradient(180deg,#6c8ab5 0%,#9db3cf 25%,#b99a82 50%,#8c5d45 75%,#6b4a3a 100%)"></div>
    <div class="label">WILDLIFE<br>PHOTOGRAPHY</div>
  </div>
  <div class="abs card" style="left:539px;top:1195px;width:170px;height:238px">
    <div class="photo" role="img" aria-label="Golden sandstone cliffs reflected in a lake" style="background:linear-gradient(180deg,#d7a05a 0%,#e4a33f 35%,#4e8e8c 55%,#c98a3a 80%,#8a5a2a 100%)"></div>
    <div class="label">LANDSCAPE</div>
  </div>
  <div class="abs card" style="left:725px;top:1195px;width:171px;height:238px">
    <div class="photo" role="img" aria-label="Joshua tree silhouette against a pink sunset" style="background:linear-gradient(180deg,#6a2d6e 0%,#d5509a 35%,#f0b0c0 50%,#7a2a55 75%,#3a1a2a 100%)"></div>
    <div class="label">SUNSETS</div>
  </div>
  <div class="abs card" style="left:907px;top:1195px;width:172px;height:238px">
    <div class="photo" role="img" aria-label="Sunrise bursting under a stone arch" style="background:linear-gradient(180deg,#4a7ab8 0%,#9fc0e0 25%,#f2c040 45%,#b05a2a 65%,#5a4a48 100%)"></div>
    <div class="label">SUNRISES</div>
  </div>
  <svg class="abs" style="left:407px;top:1446px" width="10" height="14" viewBox="0 0 10 14"><path d="M1 1 L1 11 L4 8 L6 13 L8 12 L6 7 L9 7 Z" fill="#fff"/></svg>

  <div class="abs sec-title script" style="left:-30px;top:1580px">Explore my Gallery of</div>
  <div class="abs sec-sub" style="left:691px;top:1626px">PHOTOGRAPHY</div>
  <div class="abs filters"><span class="active">ALL WORKS</span><span>FEATURES</span><span>LOCATIONS</span><span>MONUMENTS</span><span>NATURE LIFE</span></div>

  <div class="tile" style="left:209px;top:1716px;width:243px;height:184px;background:linear-gradient(180deg,#3a3aa0,#a07ad8 40%,#d6a0c0 55%,#5a4a9a)" role="img" aria-label="Crystal ball on a purple beach at dusk"></div>
  <div class="tile" style="left:209px;top:1927px;width:243px;height:147px;background:linear-gradient(180deg,#d9501f,#f39a2a 30%,#3a2a3a 50%,#a9a6d8 75%,#4a3a48)" role="img" aria-label="Sunset over snowy cliffs"></div>
  <div class="tile" style="left:209px;top:2101px;width:243px;height:280px;background:linear-gradient(180deg,#5a6a8a,#b8c0d0 25%,#9a8a8a 50%,#8a5a40 75%,#6a4a38)" role="img" aria-label="Grand canyon vista under cloudy sky"></div>
  <div class="tile" style="left:477px;top:1716px;width:242px;height:149px;background:linear-gradient(180deg,#a8b84a,#6a7a2a 40%,#5a3a2a 60%,#8a9a3a)" role="img" aria-label="Bugling elk in a green meadow"></div>
  <div class="tile" style="left:477px;top:1890px;width:242px;height:282px;background:linear-gradient(180deg,#4a7ad0,#c8d8f0 30%,#6a8ac0 50%,#2a3a3a 60%,#8aa8d8 80%,#1a2a2a)" role="img" aria-label="Clouds reflected in a river between snowy banks"></div>
  <div class="tile" style="left:477px;top:2197px;width:242px;height:184px;background:linear-gradient(180deg,#2a2e30,#3a3a38 45%,#c0602a 65%,#3a2a1e 85%,#1e1a16)" role="img" aria-label="Desert butte lit at dusk under stormy sky"></div>
  <div class="tile" style="left:746px;top:1716px;width:242px;height:282px;background:linear-gradient(180deg,#d88a8a,#f0a070 30%,#5a7ab0 55%,#2a4a8a 80%,#1a2a4a)" role="img" aria-label="Frosted blue pine branch at sunrise"></div>
  <div class="tile" style="left:746px;top:2023px;width:242px;height:149px;background:linear-gradient(180deg,#2a5ab0,#8ab0e0 45%,#c07040 70%,#6a3a28)" role="img" aria-label="Stacked rock cairn with sun star"></div>
  <div class="tile" style="left:746px;top:2197px;width:242px;height:184px;background:linear-gradient(180deg,#3a7ad0,#a0c0e8 20%,#d07a3a 45%,#a0502a 75%,#6a5a30)" role="img" aria-label="Chapel built into red rock formations"></div>

  <div class="abs btn btn-gallery">VIEW ALL GALLERY</div>

  <div class="abs sec-title script" style="left:0;top:2508px">On Snapfeed</div>
  <div class="abs insta">
    <div style="background:linear-gradient(180deg,#5a3a6a,#e08aa0 45%,#c04a5a 70%,#6a2a3a)" role="img" aria-label="Pink storm clouds over the sea"></div>
    <div style="background:linear-gradient(180deg,#d9501f,#f0902a 35%,#3a3a2a 60%,#4a6a2a)" role="img" aria-label="Sunset over a park monument"></div>
    <div style="background:radial-gradient(circle at 50% 50%,#9ab86a,#4a6a3a 50%,#2a3a2a)" role="img" aria-label="Waterfall seen through a crystal ball"></div>
    <div style="background:linear-gradient(180deg,#4a7ac0,#c8d8ea 40%,#5a6a6a 70%,#2a3a2a)" role="img" aria-label="Clouds over forested mountains"></div>
    <div style="background:linear-gradient(180deg,#d0d0c8,#c07a3a 45%,#6a8a3a 80%)" role="img" aria-label="Red fox with kit"></div>
    <div style="background:radial-gradient(circle at 55% 55%,#c08a4a,#9a9a9a 35%,#6a6a6a)" role="img" aria-label="Autumn leaf on rippling water"></div>
  </div>
  <div class="abs btn btn-follow">FOLLOW ME</div>

  <div class="abs contact" role="img" aria-label="Dark cloudy dusk sky background"></div>
  <div class="abs sec-title script" style="left:-30px;top:2975px">Let's Work Together</div>
  <div class="abs sec-sub" style="left:693px;top:3021px">ON PROJECTS</div>
  <div class="abs field" style="left:210px;top:3058px;width:243px;height:35px">Name</div>
  <div class="abs field" style="left:466px;top:3058px;width:256px;height:35px">Email</div>
  <div class="abs field" style="left:735px;top:3058px;width:256px;height:35px">Phone</div>
  <div class="abs field" style="left:210px;top:3109px;width:243px;height:35px">Location:
    <span class="icon"><svg width="10" height="13" viewBox="0 0 10 13"><path d="M5 12 C2 8 1 6 1 4.5 A4 4 0 0 1 9 4.5 C9 6 8 8 5 12 Z" fill="none" stroke="#999"/><circle cx="5" cy="4.5" r="1.4" fill="none" stroke="#999"/></svg></span>
  </div>
  <div class="abs field" style="left:210px;top:3160px;width:243px;height:35px">Photography For
    <span class="icon"><svg width="10" height="6" viewBox="0 0 10 6"><path d="M1 1 L5 5 L9 1" fill="none" stroke="#999"/></svg></span>
  </div>
  <div class="abs field tall" style="left:466px;top:3109px;width:525px;height:86px">Your Message</div>
  <div class="abs btn btn-submit">SUBMIT NOW</div>

  <div class="abs footer"></div>
  <div class="abs foot-text" style="left:214px;top:3406px;width:254px;display:flex;justify-content:center;gap:7px;align-items:center">info@marisaholloway.com
    <svg width="14" height="11" viewBox="0 0 14 11"><rect x="0" y="0" width="14" height="11" rx="1" fill="#fff"/><path d="M0.5 1 L7 6 L13.5 1" fill="none" stroke="#171717"/></svg>
  </div>
  <div class="abs foot-rule" style="left:214px;top:3442px;width:254px"></div>
  <div class="abs foot-text" style="left:214px;top:3459px;width:254px">Published by Northern Terrain</div>
  <div class="abs foot-div" style="left:478px"></div>
  <div class="abs" style="left:478px;top:3398px;width:250px;text-align:center;font-size:16px;font-weight:500">Marisa Holloway</div>
  <div class="abs social" style="left:541px;top:3455px"><span></span><span></span><span></span><span></span></div>
  <div class="abs foot-div" style="left:728px"></div>
  <div class="abs foot-text" style="left:740px;top:3406px;width:254px;display:flex;justify-content:center;gap:9px;align-items:center">
    <svg width="14" height="14" viewBox="0 0 14 14"><path d="M3 1 L5 1 L6 4 L4.5 5.5 C5.5 7.5 6.5 8.5 8.5 9.5 L10 8 L13 9 L13 11 C13 12 12 13 11 13 C5.5 12.5 1.5 8.5 1 3 C1 2 2 1 3 1 Z" fill="#fff"/></svg>
    PHONE +01-555-0142
  </div>
  <div class="abs foot-rule" style="left:740px;top:3442px;width:254px"></div>
  <div class="abs foot-text" style="left:740px;top:3459px;width:254px">Log in / Register now to Purchase</div>

  <div class="abs bottom"></div>
  <div class="abs" style="left:214px;top:3567px;font-size:8.5px;color:#cfcfcf">COPYRIGHT © 2019 M.H. PHOTOGRAPHY.COM, ALL RIGHTS RESERVED.</div>
  <div class="abs" style="left:794px;top:3567px;font-size:8.5px;color:#cfcfcf">ACCEPTED:</div>
  <div class="abs cards" style="left:855px;top:3562px"><span></span><span></span><span></span><span></span></div>

</div>
</body>
</html>
```